Outdoor sign for Brindle Auto Restoration

I need a horizontal 4'x 8' outdoor roadside sign for my classic auto restoration business. I have uploaded colors and our logo. Needs the Brindle name, a prominent Classic AUTO RESTORATION, phone number and website. We rebuild and restore vintage cars, trucks and 4x4s. I'd like something clean but possibly retro. Classic Auto Restoration is more important than the Brindle name. It needs to be visible and readable from the street. NO CLIP ART

Target Market(s)

Customers who need their vintage care restored or upgraded. Men and women ages 25-75

Industry/Entity Type

Automotive

Colors
FFC000
F8CF3A
FAE287
FDF2CF
FEFAEE

Requirements
Must have
• Legible. Bright. Readable as a backlit 4' x 8' large horizontal sign (roughly 120cm X 240cm)
Nice to have
• Use of the Brindle logo/type, Complete or Classic before prominent AUTO RESTORATION
Should not have
• Clip art of old cars or icons. And we don't want the Brindle Logo from the website because it wont be legible from the road. I have included the Illustrator file for Brindle text in the uploads

```html
<!DOCTYPE html>
<html lang="en">
<head>
<meta charset="utf-8">
<title>Brindle Auto Restoration – Roadside Sign</title>
<link href="https://fonts.googleapis.com/css2?family=Lobster&family=Oswald:wght@400;600;700&family=Roboto:wght@900&display=swap" rel="stylesheet">
<style>
  :root {
    --page: #dcdcdc;
    --sign-red: #b00c07;
    --shadow-red: #8a0a0b;
    --gold: #f5af00;
    --gold-edge: #e08a00;
    --band: #222222;
    --white: #ffffff;
  }
  html, body {
    margin: 0;
    width: 1200px;
    height: 714px;
    overflow: hidden;
    background: var(--page);
  }
  .sign {
    position: absolute;
    left: 40px;
    top: 77px;
    width: 1120px;
    height: 560px;
    display: block;
  }
  .sign-field { fill: var(--sign-red); }
  .contact-band { fill: var(--band); }
  .speed-stripe { fill: var(--gold); }
  .tagline {
    font-family: "Lobster", cursive;
    font-size: 74px;
    fill: var(--white);
  }
  .headline text {
    font-family: "Roboto", "Arial Black", sans-serif;
    font-weight: 900;
    paint-order: stroke fill;
    stroke-linejoin: round;
  }
  .auto-word { font-size: 229px; }
  .restoration-word { font-size: 134px; }
  .headline .drop-shadow {
    fill: var(--shadow-red);
    stroke: none;
  }
  .headline .auto-face {
    fill: var(--gold);
    stroke: var(--gold-edge);
    stroke-width: 3px;
  }
  .headline .restoration-face {
    fill: var(--white);
    stroke: var(--gold);
    stroke-width: 3px;
  }
  .contact-pill { fill: var(--sign-red); }
  .contact-text {
    font-family: "Oswald", "Arial Narrow", sans-serif;
    fill: var(--white);
  }
  .phone { font-weight: 600; font-size: 32px; }
  .website { font-weight: 400; font-size: 30px; }
  .business-name {
    font-family: "Oswald", "Arial Narrow", sans-serif;
    font-weight: 700;
    font-size: 90px;
    fill: var(--gold);
  }
</style>
</head>
<body>
<svg class="sign" viewBox="0 0 1120 560" xmlns="http://www.w3.org/2000/svg" role="img" aria-label="Complete Auto Restoration – Brindle – 501-555-0142 – brindleautoworks.com">
  <rect class="sign-field" x="0" y="0" width="1120" height="431"/>
  <rect class="contact-band" x="0" y="431" width="1120" height="129"/>

  <g class="speed-stripes">
    <polygon class="speed-stripe" points="0,169 310,169 308,175 0,175"/>
    <polygon class="speed-stripe" points="0,186 307,186 305,192 0,192"/>
    <polygon class="speed-stripe" points="0,203 304,203 302,209 0,209"/>
    <polygon class="speed-stripe" points="810,169 1120,169 1120,175 812,175"/>
    <polygon class="speed-stripe" points="813,186 1120,186 1120,192 815,192"/>
    <polygon class="speed-stripe" points="816,203 1120,203 1120,209 818,209"/>
  </g>

  <text class="tagline" x="557" y="84" text-anchor="middle">Complete</text>

  <g class="headline">
    <text class="auto-word drop-shadow" x="321" y="281" textLength="476" lengthAdjust="spacingAndGlyphs">AUTO</text>
    <text class="auto-word auto-face" x="309" y="272" textLength="476" lengthAdjust="spacingAndGlyphs">AUTO</text>
    <text class="restoration-word drop-shadow" x="106" y="414" textLength="932" lengthAdjust="spacingAndGlyphs">RESTORATION</text>
    <text class="restoration-word restoration-face" x="94" y="405" textLength="932" lengthAdjust="spacingAndGlyphs">RESTORATION</text>
  </g>

  <rect class="contact-pill" x="38" y="473" width="297" height="46" rx="4"/>
  <text class="contact-text phone" x="59" y="510" textLength="255" lengthAdjust="spacing">501-555-0142</text>

  <text class="business-name" x="356" y="532" textLength="408" lengthAdjust="spacingAndGlyphs">BRINDLE</text>

  <rect class="contact-pill" x="783" y="473" width="296" height="46" rx="4"/>
  <text class="contact-text website" x="801" y="508" textLength="260" lengthAdjust="spacingAndGlyphs">brindleautoworks.com</text>
</svg>
</body>
</html>
```